Simple, Professional and neat business card design for Vellamor Inc.

We're looking to re-vamp our business card design. We're a supplier of innovative feed ingredients for the North American animal agriculture industry. We are located in Lucknow, Ontario, Canada and our flagship product is a product that prevents milk fever in dairy cows when the calve, it is fed before calving and is very effective compared to other alternatives available on the market today.

Our company has Danish roots and we import all of our product from our Danish partner/manufacturer in Denmark. We like our design to embrace high professionalism while remaining neat and simple.

Target Market(s)

B2B, Feed Mills, Veterinary Clinics, Large integrators/producers,

Industry/Entity Type

Agribusiness

Contact Information for Business Card

We like the rounded corners because they make the card easy to sit in a wallet and not many use it so it makes the card stand out, just possibly something to take account for during the design.

As you can also see on the sliders below, looking for a that simple but proffesional scandinavian design.

Requirements
Nice to have
• Rounded corners
Should not have
• Too vibrant

```html
<!DOCTYPE html>
<html lang="en">
<head>
<meta charset="utf-8">
<title>Vellamor Inc. — Business Card</title>
<link href="https://fonts.googleapis.com/css2?family=Lato:wght@900&family=Montserrat:wght@400;600&display=swap" rel="stylesheet">
<style>
  :root {
    --bg: #1c1c1c;
    --card-white: #ffffff;
    --brand-blue: #0d50a0;
    --back-blue: #0b5aa6;
    --ink: #2b2b2b;
    --white: #ffffff;
  }
  html, body {
    margin: 0; padding: 0;
    width: 1200px; height: 897px;
    overflow: hidden;
    background: var(--bg);
  }
  .card {
    position: absolute;
    left: 303px;
    width: 595px; height: 339px;
    border-radius: 22px;
    overflow: hidden;
  }
  .card--front {
    top: 92px;
    background: radial-gradient(circle at 500px 60px, #f4f5f7 0, #f7f8f9 90px, var(--card-white) 170px);
  }
  .card--back { top: 469px; background: var(--back-blue); }

  .brand-dot {
    position: absolute;
    border-radius: 50%;
  }
  .card--front .brand-dot { left: 30px; top: 32px; width: 72px; height: 72px; background: var(--brand-blue); }
  .card--back .brand-dot { left: 94px; top: 131px; width: 76px; height: 76px; background: var(--white); }

  .brand-name {
    position: absolute;
    margin: 0;
    font-family: "Lato", sans-serif;
    font-weight: 900;
    font-size: 45px;
    letter-spacing: -0.5px;
    line-height: 1;
    white-space: nowrap;
  }
  .card--front .brand-name { left: 125px; top: 50px; color: var(--brand-blue); }
  .card--back .brand-name { left: 189px; top: 152px; color: var(--white); }

  .person-name {
    position: absolute; left: 30px; top: 164px; margin: 0;
    font-family: "Montserrat", sans-serif; font-weight: 600;
    font-size: 21px; color: var(--brand-blue); line-height: 1;
  }
  .person-role {
    position: absolute; left: 30px; top: 190px; margin: 0;
    font-family: "Montserrat", sans-serif; font-weight: 400;
    font-size: 14.5px; color: var(--ink); line-height: 1;
  }
  .divider {
    position: absolute; left: 30px; top: 218px;
    width: 540px; height: 2px; background: var(--brand-blue);
  }
  .contact {
    position: absolute; margin: 0; padding: 0; list-style: none;
    font-family: "Montserrat", sans-serif; font-weight: 400;
    font-size: 14.5px; color: var(--ink);
  }
  .contact li { display: flex; align-items: center; height: 20px; white-space: nowrap; }
  .contact svg { width: 11px; height: 11px; margin-right: 7px; flex: none; fill: var(--brand-blue); }
  .contact--phones { left: 30px; top: 237px; }
  .contact--web { left: 371px; top: 233px; }
  .address {
    position: absolute; left: 371px; top: 279px; margin: 0;
    font-family: "Montserrat", sans-serif; font-weight: 400; font-style: normal;
    font-size: 14.5px; line-height: 19px; color: var(--ink);
  }
</style>
</head>
<body>

<section class="card card--front">
  <span class="brand-dot"></span>
  <h1 class="brand-name">VELLAMOR INC.</h1>

  <p class="person-name">Anders Holmgaard</p>
  <p class="person-role">Founder</p>
  <div class="divider"></div>

  <ul class="contact contact--phones">
    <li><svg viewBox="0 0 12 12"><path d="M2.5 0.5l2 2.5-1 1.2c.6 1.5 1.8 2.7 3.3 3.3l1.2-1 2.5 2-1.2 2.5C5 10.8 1.2 7 0 2.2z"/></svg>519-402-1186</li>
    <li><svg viewBox="0 0 12 12"><path d="M3 0h6a1 1 0 0 1 1 1v10a1 1 0 0 1-1 1H3a1 1 0 0 1-1-1V1a1 1 0 0 1 1-1zm.5 1.5v7.5h5V1.5z"/></svg>519-604-7731</li>
    <li><svg viewBox="0 0 12 12"><path d="M3 0h6v3H3zM0 4h12v5h-2v3H2V9H0zm3 4v3h6V8z"/></svg>519-604-7740</li>
    <li><svg viewBox="0 0 12 12"><path d="M0 4c2-3 10-3 12 0l-1 2H9V4.5H3V6H1zM2 7h8l1 5H1zm4 1.5a1.5 1.5 0 1 0 0 3 1.5 1.5 0 0 0 0-3z"/></svg>888-315-2079 (Toll Free)</li>
  </ul>

  <ul class="contact contact--web">
    <li><svg viewBox="0 0 12 12"><path d="M0 2h12v8H0zm1.3 1.2v5.6h9.4V3.2L6 6.3zM2 3.2L6 5.6l4-2.4z"/></svg>anders@vellamor.com</li>
    <li><svg viewBox="0 0 12 12"><path d="M6 0a6 6 0 1 0 0 12A6 6 0 0 0 6 0zm-.6 1.3v2.2H3.6c.4-1.1 1-1.9 1.8-2.2zm1.2 0c.8.3 1.4 1.1 1.8 2.2H6.6zM2.3 3.5H2.5a4.8 4.8 0 0 0 0 0zM1.3 4.7h2c-.1.8-.1 1.8 0 2.6h-2a4.7 4.7 0 0 1 0-2.6zm3.2 0h3c.1.8.1 1.8 0 2.6h-3c-.1-.8-.1-1.8 0-2.6zm4.2 0h2a4.7 4.7 0 0 1 0 2.6h-2c.1-.8.1-1.8 0-2.6zM3.6 8.5h1.8v2.2c-.8-.3-1.4-1.1-1.8-2.2zm3 0h1.8c-.4 1.1-1 1.9-1.8 2.2z"/></svg>www.vellamor.com</li>
  </ul>

  <address class="address">Box 412, Brookfield,<br>Ontario Canada N0M 3K1</address>
</section>

<section class="card card--back">
  <span class="brand-dot"></span>
  <h2 class="brand-name">VELLAMOR INC.</h2>
</section>

</body>
</html>
```